Vorel constructions

We are predominantly a residential home builder based in Melbourne, Victoria Australia. We construct houses, apartments, townhouses, multi-unit developments.

The name of the company is "Vorel Constructions"
My company believes in building unique construction projects mainly residential homes. The target customers are upmarket Melbourne residents/investors.

I want the brand name "Vorel" to be part of the logo. There's no need to put the word construction in the logo at this stage.

I would also like some ideas for a slogan e.g. "Just build it." or "We build quality homes." But I would like something unique and different for a slogan not the same old cliche.

vorelconstructions.example.com.au
e: tmelo@vorelconstructions.example.com.au
M: 0417305862
Address: 8/3 Fenwick Lane Clayton VIC 3168

Director:Mr Dinesh Malarkodiyan

```html
<!DOCTYPE html>
<html lang="en">
<head>
<meta charset="utf-8">
<title>Vorel Constructions – Business Card</title>
<link href="https://fonts.googleapis.com/css2?family=Lato:wght@400;700;900&display=swap" rel="stylesheet">
<style>
  :root {
    --navy: #1f2a5e;
    --sky: #2aa8e0;
    --ink: #1d1d1f;
    --paper: #ffffff;
    --backdrop: #e6e9eb;
    --muted: #555a63;
  }
  * { box-sizing: border-box; margin: 0; padding: 0; }
  html, body {
    width: 1200px; height: 1000px; overflow: hidden;
    background: var(--backdrop);
    font-family: "Lato", Arial, sans-serif;
  }
  .canvas { position: relative; width: 1200px; height: 1000px; }
  .card {
    position: absolute; left: 250px; width: 700px; height: 400px;
    background: var(--paper);
    box-shadow: 0 6px 18px rgba(0,0,0,.18);
    overflow: hidden;
  }
  .card--front { top: 70px; }
  .card--back { top: 530px; }

  /* front */
  .front-band {
    position: absolute; left: 0; top: 0; width: 100%; height: 160px;
    background: var(--navy);
    border-bottom: 4px solid var(--sky);
  }
  .brand {
    position: absolute; display: flex; align-items: center; gap: 10px;
    color: var(--sky); font-weight: 900; letter-spacing: 1px; white-space: nowrap;
  }
  .brand__mark { width: 18px; height: 18px; background: var(--sky); }
  .front-band .brand { left: 48px; top: 62px; font-size: 44px; }
  .tagline {
    position: absolute; color: var(--paper); font-weight: 700; font-size: 17px; white-space: nowrap;
  }
  .front-band .tagline { left: 48px; top: 122px; }

  .director {
    position: absolute; right: 48px; top: 186px; text-align: right;
  }
  .director__name { font-size: 21px; font-weight: 700; color: var(--ink); }
  .director__role { font-size: 15px; color: var(--muted); margin-top: 4px; }

  .contact { position: absolute; left: 48px; top: 232px; }
  .contact__company { font-size: 21px; font-weight: 900; color: var(--ink); }
  .contact__address { font-size: 15px; color: var(--muted); margin: 4px 0 14px; }
  .contact__row {
    display: flex; align-items: center; gap: 12px;
    font-size: 15px; color: var(--ink); margin-bottom: 7px;
  }
  .contact__row svg { width: 16px; height: 16px; flex: none; }

  /* back */
  .back-band {
    position: absolute; left: 0; top: 125px; width: 100%; height: 150px;
    background: var(--navy);
  }
  .back-band .brand { left: 50%; transform: translateX(-50%); top: 30px; font-size: 46px; }
  .back-band .tagline { left: 0; width: 100%; text-align: center; top: 98px; font-size: 18px; }
</style>
</head>
<body>
<main class="canvas">

  <section class="card card--front" aria-label="Business card front">
    <div class="front-band">
      <div class="brand"><span class="brand__mark"></span>vorel</div>
      <p class="tagline">Homes Shaped Around the Way You Live</p>
    </div>

    <div class="director">
      <p class="director__name">Mr Dinesh Malarkodiyan</p>
      <p class="director__role">Director</p>
    </div>

    <div class="contact">
      <p class="contact__company">VOREL CONSTRUCTIONS</p>
      <p class="contact__address">8/3 Fenwick Lane Ashcombe VIC 3190</p>
      <p class="contact__row">
        <svg viewBox="0 0 16 16" aria-hidden="true"><path d="M3 1h3l1.5 4-2 1.3a9 9 0 0 0 4.2 4.2L11 8.5l4 1.5v3a2 2 0 0 1-2 2A12 12 0 0 1 1 3a2 2 0 0 1 2-2z" fill="var(--ink)"/></svg>
        0417305862
      </p>
      <p class="contact__row">
        <svg viewBox="0 0 16 16" aria-hidden="true"><rect x="1" y="3" width="14" height="10" fill="var(--ink)"/><path d="M1 3l7 6 7-6" fill="none" stroke="#fff" stroke-width="1.4"/></svg>
        tmelo@vorelconstructions.example.com.au
      </p>
      <p class="contact__row">
        <svg viewBox="0 0 16 16" aria-hidden="true"><circle cx="8" cy="8" r="6.5" fill="none" stroke="var(--ink)" stroke-width="1.6"/><path d="M1.5 8h13M8 1.5c-3 3-3 10 0 13M8 1.5c3 3 3 10 0 13" fill="none" stroke="var(--ink)" stroke-width="1.2"/></svg>
        vorelconstructions.example.com.au
      </p>
    </div>
  </section>

  <section class="card card--back" aria-label="Business card back">
    <div class="back-band">
      <div class="brand"><span class="brand__mark"></span>vorel</div>
      <p class="tagline">Homes Shaped Around the Way You Live</p>
    </div>
  </section>

</main>
</body>
</html>
```